Service Transporter Design // Vehicle Branding Project*

We need a sticker design for our service vehicle based on our current one (see attached) for a company based in Berlin Germany called VOSKE Grossküchentechnik. We are selling professional industrial kitchen equipment.

Vehicle Type: Halvard Trekker M

We would like the design to be edgy and confident. We would prefer the sticker design to utilize the colors on our logo (see attached). White is the color of the vehicle.

Please take a closer look to file 3, a sample which we like!

Furthermore, we would be glad to jump on new trend like transport our business with the help of icons or symbols i.e. a shopping cart icon for our online shop.

In addition for that, we are looking for a service technician in our city.
Therefore it would be helpful to place a banner (3 sides) for it with the following information:

Kollege gesucht
Bewerbungen erwünscht!

in addition to that

Telephon: 030 / 71 28 94 3 05
Email: service@voske-kuechenhaus.de
Shop: www.voske-kuechenhaus.de
24h

Our company has been one of the well-known and powerful companies in our industry in Berlin and Brandenburg. It was founded in 1926 as a trade company for heating systems and oriented after 1945 to the field of cooking equipment for commercial kitchens.

The purchased in 30 years of service expertise, we have developed into a leader in the engineering industry, food service in Berlin and could extend this position even after the reunification of the surrounding area in the state of Brandenburg.

Our ambition is not to be the cheapest provider in the lowest-price segment. Our mission is to provide our partners with well-known, enduring brand makes and accompanying maintenance service, the basic conditions for a long-term economic success.

We utilize the expertise of powerful manufacturing companies with long experience in concretizing of caterers.

We would like the sticker to be modern, clean and professional, and should utilize the colors cyan white and grey.

Our website is: http://www.voske-kuechenhaus.de

Your are welcome to impress us!

Reason: not 100% percent conviced of the current work. please do better and give you best! Thank you

Hello Designers!

Please be welcome again to make a Design in this direction combined with our new logo:

Reason: Hello Designers! Your welcome again to precise the Car Design as mentioned in my comments with the blue & white example please make some stunning designs! thx! torvald

please take a closer look on sample design file:

Today of have a meeting about all your design proposals.
Will give you feedback by today.

Thx, Torvald

Hallo Designer,

 

First of all, thank so much for the nice ideas from you!

We made ??yesterday comprehensive thoughts about the designconcept of our service vehicles and have come to the conclusion that we reallywant to communicate our brand more "VOSKE".

 

How do we imagine the now proposing?

The logo we want to be more larger at all on the vehicle.

Our business fields are more stroken by icons/symbols on thesideview and backview.

topics:

REPERATURSERVICE(repair service) KOCHGERÄTE (coookingmachines) – KÜHLGERÄTE (cooling machines)– SPÜLMSCHINEN (professional dishwaher) - if there is more room, you canplace also a coffeemchines (professional one)

for each topic we need a
pregnant symbol, butwith no comparison to home machines>> industrial machines.

please have a look on attached new Pdf for the concept of content

I will extent the project for more 7 days, I would be very thankfull, if you provide me a new direction :-)

Thank you!

Torvald

Reason: Hallo Designer, First of all, thank so much for the nice ideas from you! We made yesterday comprehensive thoughts about the design concept of our service vehicles and have come to the conclusion that we really want to communicate our brand more "VOSKE". How do we imagine the now proposing? The logo we want to be more larger at all on the vehicle. Our business fields are more stroken by icons/symbols on the sideview and backview. topics: REPERATURSERVICE (repair service) KOCHGERÄTE (coookingmachines) – KÜHLGERÄTE (cooling machines) – SPÜLMSCHINEN (professional dishwaher) - if there is more room, you can place also a coffeemchines (professional one) for each topic we need a pregnant symbol, but with no comparison to home machines >> industrial machines. please be so kind and read new additional concept in pdf

Target Market(s)

Hotels, Hospital, Restaurants, professional kitchen

Industry/Entity Type

Industrial

Requirements
Must have
• all in our colors:
white (I know, it not a color, cyan (like in logo file) and grey

icons & symbols
Nice to have
• impressive Photo, eye catcher

```html
<!DOCTYPE html>
<html lang="de">
<head>
<meta charset="utf-8">
<title>VOSKE Grossküchentechnik – Fahrzeugbanner</title>
<link rel="stylesheet" href="https://fonts.googleapis.com/css2?family=Arimo:ital,wght@0,400;0,700;1,700&family=PT+Sans&display=swap">
<style>
  :root {
    --stage: #e4e5e7;
    --white: #ffffff;
    --cyan: #1b9fe0;
    --navy: #1f2a5c;
    --grey: #6d6e70;
    --yellow: #f4ee1c;
    --edge: #d0d2d4;
  }
  html, body {
    margin: 0;
    width: 1200px;
    height: 900px;
    overflow: hidden;
    background: var(--stage);
  }
  .banner {
    position: absolute;
    left: 216px;
    top: 303px;
    width: 768px;
    height: 294px;
    display: block;
  }
  .banner-face { fill: var(--white); stroke: var(--edge); stroke-width: 1; }
  .accent-wedge { fill: var(--cyan); }
  .phone-band { fill: var(--navy); }
  .brand-name {
    font-family: "Arimo", Arial, sans-serif;
    font-weight: 700;
    font-size: 72px;
    fill: var(--cyan);
  }
  .brand-descriptor {
    font-family: "PT Sans", Verdana, sans-serif;
    font-size: 27px;
    fill: var(--grey);
  }
  .brand-rule { stroke: var(--cyan); stroke-width: 2; }
  .web-address {
    font-family: "Arimo", Arial, sans-serif;
    font-weight: 700;
    font-size: 30px;
    fill: var(--cyan);
  }
  .phone-number {
    font-family: "Arimo", Arial, sans-serif;
    font-weight: 700;
    font-size: 39px;
    fill: var(--white);
  }
  .service-badge { fill: url(#badgeFill); stroke: var(--white); stroke-width: 3; }
  .hiring-call {
    font-family: "Arimo", Arial, sans-serif;
    font-weight: 700;
    font-style: italic;
    font-size: 16px;
    fill: var(--white);
  }
  .hiring-call--accent { fill: var(--yellow); }
</style>
</head>
<body>
<svg class="banner" viewBox="0 0 768 294" xmlns="http://www.w3.org/2000/svg">
  <defs>
    <radialGradient id="badgeFill" cx="50%" cy="45%" r="60%">
      <stop offset="0%" stop-color="#ffffff"/>
      <stop offset="100%" stop-color="#8fcdf0"/>
    </radialGradient>
  </defs>

  <rect class="banner-face" x="0.5" y="0.5" width="767" height="293"/>
  <polygon class="accent-wedge" points="423,294 768,47 768,294"/>
  <rect class="phone-band" x="0" y="230" width="768" height="57"/>

  <text class="brand-name" x="40" y="96" textLength="470" lengthAdjust="spacing">VOSKE</text>
  <text class="brand-descriptor" x="38" y="148" textLength="472" lengthAdjust="spacing">Grossküchentechnik</text>
  <line class="brand-rule" x1="38" y1="164" x2="511" y2="164"/>

  <text class="web-address" x="46" y="209" textLength="426" lengthAdjust="spacingAndGlyphs">www.voske-kuechenhaus.de</text>
  <text class="phone-number" x="199" y="272" textLength="367" lengthAdjust="spacingAndGlyphs">(030) 71 28 94 3 05</text>

  <g role="img" aria-label="Runde 24h-Servicemobil-Plakette">
    <circle class="service-badge" cx="660" cy="92" r="66"/>
  </g>

  <text class="hiring-call" x="672" y="193" text-anchor="middle">Kollege Gessucht!</text>
  <text class="hiring-call hiring-call--accent" x="672" y="215" text-anchor="middle">Bitte Melden</text>
</svg>
</body>
</html>
```